ECommerce Site Redesign: overall site and specific pages

We have a website that has been in operation for 6+ years, and it's time for a visual refresh.

Our current website is located at http://trx.example

The only significant functional change will be the movement of the persistent vertical navigation bar from the left side up to a categorized horizontal navigation menu. I've attached a rough mockup of how we want this positioned.

No coding necessary; just PSDs. The attached ROUGH MENU MOCKUP.PSD contains a layer with our logo on white should you wish to include it in your submissions.

Target Market(s)

We are an outdoor retailer focused on the high end of the market. We have a general color scheme on our site which we'd like to keep, but various elements need to be made consistent and more aesthetically pleasing.

Our brand is very important to us, and the site design must reflect our values of high quality and affluence. We cater to outdoor enthusiasts, hikers, back packers, and general high end apparel consumers.

Requirements
Must have
• In order to address the issue of consistency, we require strict design guidelines, including font sizing, element spacing, etc.

We require 7 page design templates for:

1.) overall site template - see http://trx.example for current.
* narrow static header bar (NEW)
* footer (KEEP SAME/SIMILAR)
* background
* body
* mini-cart (collapsed and expanded)
* promotion panel (ad box, rotating featured items)
* horizontal navigation bars (expanded/collapsed, grouped by 7 main categories) - see attached ROUGH MENU MOCKUP and see additional notes.
* recently viewed products

2.) product page (see http://trx.example/270599/frostline_heritage-cowl-true-max-mens.aspx for current)
* product imagery/zoombox
* color, size, quantity selection
* add to cart button
* detail tabs
* In-store Availability info
* info panel near the add to cart box for exceptions including:
- Available to pick up in-store only
- Free shipping for your entire order when you purchase this item
- This item is over-sized; please contact a store directly
* "customers who bought this also bought" panel, grid listing of items

3.) product listings (category, search results, etc.)
* item thumbnails in grid format
* sidebar for refinement options (by supplier, by price, by size, etc.)

4.) generic information/content page (see http://trx.example/t-returns.aspx)

5.) store locations page (see http://trx.example/t-TRX.stores.04.aspx)
* store details
* map
* hours
* contact info
* local links
* contact form

6.) contact us form

7.) checkout (see attached current checkout screen shot)
* cart summary
* checkout steps

Any visual elements benefiting from hover effects will need to have both dimmed and hovered layers in the design.

```html
<!DOCTYPE html>
<html lang="en">
<head>
<meta charset="utf-8">
<title>Tundra Ridge Outfitters – BackPacks</title>
<link href="https://fonts.googleapis.com/css2?family=Arimo:ital,wght@0,400;0,700;1,400&family=Gelasio:wght@400&display=swap" rel="stylesheet">
<style>
:root{
  --purple:#8b62ad;
  --purple-dark:#6f4a94;
  --purple-soft:#b89bd0;
  --blue:#1467b5;
  --link:#1a6fc2;
  --sky:#bcd9ee;
  --ink:#333;
  --grey:#555;
  --white:#fff;
  --line:#c9c9c9;
}
*{box-sizing:border-box;margin:0;padding:0}
html,body{width:995px;height:1200px;overflow:hidden}
body{position:relative;background:var(--white);font-family:"Arimo",Arial,sans-serif;color:var(--ink)}
.abs{position:absolute}

.topbar{left:0;top:0;width:995px;height:45px;background:var(--purple)}
.topbar .util{left:124px;top:19px;font-size:11px;color:var(--white);letter-spacing:.2px}
.topbar .cart{left:634px;top:19px;font-size:11px;color:var(--white)}
.checkout{left:810px;top:14px;width:74px;height:22px;border-radius:4px;background:linear-gradient(#5fc3f0,#1c8fd6);color:var(--white);font-size:10px;font-weight:700;text-align:center;line-height:22px;letter-spacing:.3px}

.header{left:0;top:45px;width:995px;height:131px;background:linear-gradient(#fff 0%,#fff 35%,#dbeaf6 75%,#a9cde9 100%)}
.brand{left:124px;top:64px;font-size:30px;font-weight:700;color:var(--purple);letter-spacing:1px;line-height:1}
.brand-sub{left:168px;top:98px;font-size:8px;font-weight:700;color:var(--purple);letter-spacing:13px}
.search{left:638px;top:65px;width:248px;height:26px;border:1px solid #c4c4c4;border-radius:4px;background:var(--white);overflow:hidden}
.search span{position:absolute;left:8px;top:7px;font-size:9px;font-style:italic;color:#aaa}
.search .go{position:absolute;right:0;top:0;width:28px;height:24px;background:linear-gradient(#5cb8ee,#1a7fcc)}
.nav{left:124px;top:143px;width:760px;display:flex;font-size:13px;color:#111}
.nav span{padding:0 20px 0 24px}
.nav i{font-style:normal;color:#333}
.nav-rule{left:124px;top:162px;width:760px;height:3px;background:linear-gradient(90deg,transparent,rgba(90,110,130,.55) 10%,rgba(90,110,130,.55) 90%,transparent)}

.hero{left:0;top:176px;width:995px;height:138px;background:linear-gradient(#9fb8cf,#e9eef3 45%,#c8d2dc 80%,#8f9aa5)}

.sidebar{left:125px;top:338px;width:193px;height:512px;border-radius:10px;background:linear-gradient(#fff 0%,#fff 12%,#d7e8f5 40%,#b8d6ee 100%);box-shadow:0 1px 4px rgba(0,0,0,.3)}
.cat{left:118px;width:190px;height:27px;background:var(--blue);color:var(--white);font-family:"Gelasio",Georgia,serif;font-size:14px;line-height:27px;padding-left:23px}
.cat b{position:absolute;left:154px;top:0;font-family:"Arimo",Arial,sans-serif;font-weight:400;font-size:11px}
.cat.active{background:var(--purple-soft)}

.title{left:342px;top:341px;font-size:24px;font-weight:700;color:var(--purple)}
.title-icon{left:476px;top:333px;width:26px;height:34px;border-radius:10px 10px 5px 5px;background:linear-gradient(#c9a6e0,#7d4fa3)}
.intro{left:342px;top:375px;width:540px;font-size:12px;line-height:17.1px;color:var(--grey)}

.brands{left:336px;top:494px;width:549px;height:64px;border:2px solid #d2d2d2;border-radius:10px;background:linear-gradient(#fff,#f1f1f1)}
.brands .arrow{position:absolute;top:12px;width:12px;height:36px}
.brand-name{position:absolute;top:25px;width:80px;text-align:center;font-size:10px;font-weight:700;color:#333}

.subcats{left:336px;top:592px;width:147px}
.subcats li{list-style:none;height:23.5px;border-bottom:1px dotted #bbb;font-size:12.5px;color:var(--link);line-height:24px}
.subcats li::before{content:"»";color:var(--purple);font-size:10px;margin-right:6px}

.card{width:84px;height:128px;border-radius:6px;background:var(--white);box-shadow:0 0 3px rgba(0,0,0,.35);overflow:hidden}
.card .photo{position:absolute;left:14px;top:12px;width:56px;height:66px;border-radius:14px 14px 8px 8px}
.card .label{position:absolute;left:0;bottom:0;width:84px;height:39px;background:var(--purple);color:var(--white);font-size:10px;text-align:center;line-height:14.5px;padding-top:5px}

.footer{left:0;top:882px;width:995px;height:318px;border-top:2px solid var(--blue);background:linear-gradient(#fff 0%,#f1ebf6 35%,#c5afd9 75%,#9a78bc 100%)}
.f-brand{left:120px;top:912px;font-size:24px;font-weight:700;color:var(--purple);letter-spacing:1px;line-height:1}
.f-brand-sub{left:156px;top:938px;font-size:6px;font-weight:700;color:var(--purple);letter-spacing:10px}
.f-rule{left:118px;width:216px;height:1px;background:var(--purple-soft)}
.f-link{left:160px;font-size:10px;color:#222;line-height:12.5px;width:160px}
.f-icon{left:126px;width:28px;height:28px;border-radius:4px;background:#3c5f9c}
.f-head{font-size:10px;color:#222}
.f-col{font-size:10px;color:#444;line-height:18.6px;letter-spacing:.3px}
.f-note{left:370px;top:1091px;font-size:10px;font-style:italic;color:#111}
.copy{left:0;top:1172px;width:995px;text-align:center;font-size:10px;color:var(--white)}
</style>
</head>
<body>

<div class="abs topbar">
  <div class="abs util">FIND A STORE &nbsp;| CONTACT US &nbsp;| Ph.888-555-0142</div>
  <div class="abs cart">There are &nbsp;items in your cart. $0.00</div>
  <div class="abs checkout">CHECKOUT</div>
</div>

<div class="abs header"></div>
<div class="abs brand">TUNDRA RIDGE</div>
<div class="abs brand-sub">OUTFITTERS</div>
<div class="abs search"><span>serch entire store here...</span>
  <div class="go"><svg width="28" height="24" viewBox="0 0 28 24"><circle cx="15" cy="10" r="5" fill="none" stroke="#fff" stroke-width="2"/><line x1="11.5" y1="13.5" x2="8" y2="17" stroke="#fff" stroke-width="2.5" stroke-linecap="round"/></svg></div>
</div>
<nav class="abs nav">
  <span>Home</span><i>|</i><span>Women</span><i>|</i><span>Men</span><i>|</i><span>Gears</span><i>|</i><span>Ultralight</span><i>|</i><span>Inspire</span><i>|</i><span>Reviews</span><i>|</i><span>On Sale</span>
</nav>
<div class="abs nav-rule"></div>

<div class="abs hero" role="img" aria-label="Two hikers with trekking poles standing on a rocky summit above a sea of clouds"></div>

<aside class="abs sidebar"></aside>
<div class="abs cat" style="top:354px">Sunglasses<b>113</b></div>
<div class="abs cat active" style="top:386px">BackPacks<b>36</b></div>
<div class="abs cat" style="top:419px">Hydration<b>395</b></div>
<div class="abs cat" style="top:452px">Tents &amp; Traps<b>53</b></div>
<div class="abs cat" style="top:485px">Sleeping Bags<b>88</b></div>
<div class="abs cat" style="top:517px">Camp Kitchen<b>34</b></div>
<div class="abs cat" style="top:549px">Rops &amp; Cordage<b>93</b></div>

<h1 class="abs title">BackPacks</h1>
<div class="abs title-icon" role="img" aria-label="Purple backpack icon"></div>
<p class="abs intro">Lorem ipsum dolor sit amet, consectetur adipiscing elit. Aliquam semper ligula a arcu rutrum sit amet imperdiet tellus viverra. Vestibulum ante ipsum primis in faucibus orci luctus et ultrices posuere cubilia Curae; Vivamus sapien turpis, sodales sed placerat vel, iaculis ut lorem. Curabitur at tempor mauris. Nulla in rutrum sem. Fusce ultrices tortor id risus ullamcorper sed placerat sem dignissim. Fusce faucibus turpis sed dui cursus congue vel vitae diam. Proin pharetra commodo ligula eu bibendum. Quisque vitae dui vitae urna fringilla tempor eget eu odio. Curabitur tincidunt augue vel.</p>

<div class="abs brands">
  <svg class="arrow" style="left:8px" viewBox="0 0 12 36"><polyline points="10,2 3,18 10,34" fill="none" stroke="#bbb" stroke-width="3"/></svg>
  <div class="brand-name" style="left:28px">Crestline</div>
  <div class="brand-name" style="left:115px">Vortal</div>
  <div class="brand-name" style="left:202px">Nordvik</div>
  <div class="brand-name" style="left:289px">Kestrel Gear</div>
  <div class="brand-name" style="left:376px">Alpenhorn</div>
  <div class="brand-name" style="left:455px">Slate Peak</div>
  <svg class="arrow" style="right:8px" viewBox="0 0 12 36"><polyline points="2,2 9,18 2,34" fill="none" stroke="#bbb" stroke-width="3"/></svg>
</div>

<ul class="abs subcats">
  <li>Day Packs</li><li>Packs Over 4oL</li><li>Travel Bags</li><li>Lumbar Packs</li><li>Backpack Accessories</li><li>Child Carriers</li>
</ul>

<div class="abs card" style="left:510px;top:578px"><div class="photo" role="img" aria-label="Black daypack" style="background:#2a2a2a"></div><div class="label">$99.95(CAD)<br>Ridge Runner</div></div>
<div class="abs card" style="left:605px;top:578px"><div class="photo" role="img" aria-label="Dark teal backpack" style="background:#28434a"></div><div class="label">$99.95(CAD)<br>Ridge Runner</div></div>
<div class="abs card" style="left:700px;top:578px"><div class="photo" role="img" aria-label="Grey and red sling pack" style="background:linear-gradient(#7a7a7a,#b23040)"></div><div class="label">$99.95(CAD)<br>Ridge Runner</div></div>
<div class="abs card" style="left:795px;top:578px"><div class="photo" role="img" aria-label="Orange climbing pack" style="background:#f0521c"></div><div class="label">$99.95(CAD)<br>Ridge Runner</div></div>

<div class="abs card" style="left:510px;top:729px"><div class="photo" role="img" aria-label="Blue hiking pack" style="background:#1c7fd6"></div><div class="label">$99.95(CAD)<br>Ridge Runner</div></div>
<div class="abs card" style="left:605px;top:729px"><div class="photo" role="img" aria-label="Black expedition pack" style="background:#1f1f1f"></div><div class="label">$99.95(CAD)<br>Ridge Runner</div></div>
<div class="abs card" style="left:700px;top:729px"><div class="photo" role="img" aria-label="Green duffel pack" style="background:#3dbd3a"></div><div class="label">$99.95(CAD)<br>Ridge Runner</div></div>
<div class="abs card" style="left:795px;top:729px"><div class="photo" role="img" aria-label="Yellow alpine pack" style="background:#e6d12a"></div><div class="label">$99.95(CAD)<br>Ridge Runner</div></div>

<footer class="abs footer"></footer>
<div class="abs f-brand">TUNDRA RIDGE</div>
<div class="abs f-brand-sub">OUTFITTERS</div>
<div class="abs f-rule" style="top:949px"></div>
<div class="abs f-icon" style="top:962px"></div>
<div class="abs f-link" style="top:964px">Tundra Ridge Outfitters on Socialnet</div>
<div class="abs f-rule" style="top:998px"></div>
<div class="abs f-icon" style="top:1003px;background:#b9a89a" role="img" aria-label="Portrait of the company president"></div>
<div class="abs f-link" style="top:1007px">Message from our President</div>
<div class="abs f-rule" style="top:1038px"></div>
<div class="abs f-icon" style="top:1043px;background:#3f6fb3"><svg width="28" height="28" viewBox="0 0 28 28"><rect x="5" y="8" width="18" height="12" fill="none" stroke="#fff" stroke-width="1.5"/><polyline points="5,8 14,15 23,8" fill="none" stroke="#fff" stroke-width="1.5"/></svg></div>
<div class="abs f-link" style="top:1049px">Email our president</div>
<div class="abs f-rule" style="top:1077px"></div>

<div class="abs f-head" style="left:378px;top:949px">Tundra Ridge Stores</div>
<div class="abs f-col" style="left:386px;top:971px">Abbotsford<br>Canmore<br>Courtenay<br>Medicine Hat<br>Nanaimo<br>Nelson</div>
<div class="abs f-col" style="left:504px;top:971px">New Denver<br>Red Deer<br>Revelstoke<br>Smithers<br>Squamish<br>Vancouver</div>
<div class="abs f-note">Each shop is locally owned and operated</div>

<div class="abs f-head" style="left:620px;top:949px">Site Services</div>
<div class="abs f-col" style="left:622px;top:971px">Privacy and<br>Security<br>Return Policy<br>Shipping Rates<br>Terms &amp;<br>Conditions<br>Site Map</div>

<div class="abs f-head" style="left:746px;top:949px">About TRX</div>
<div class="abs f-col" style="left:746px;top:962px">About Us<br>Frequently Asked<br>Questions<br>Contact Us</div>
<div class="abs f-head" style="left:746px;top:1045px">My TRX</div>
<div class="abs f-col" style="left:746px;top:1058px">My TRX Account<br>Info<br>My Address<br>Change</div>

<div class="abs copy">(C) 2012 Tundra Ridge Outfitters Inc. ALL RIGHTS RESERVED</div>

</body>
</html>
```